Dental Business Card

I need Dental oriented business cards.
On the front side -
- on the first line, my name:
Dr Marlo Vintner
- on the second line (just underneath):
Doctor of Dental Medicine
- on the third line, or underneath that or in a corner, I would like the address and phone number:
5182 Ch. Birchfield
Montreal QC H2T 4B9
514-629-5074
- other than that i would maybe like a logo of a tooth, but i want it to be subtle and very basic!
- I would like the card to be preferably black or dark grey-ish with the writing in white
On the other side -
- 2-3 lines with the possibility to write the next appointment the box with the lines should be white, with the rest of the card being black

```html
<!DOCTYPE html>
<html lang="en">
<head>
<meta charset="utf-8">
<title>Dr Marlo Vintner – Business Card</title>
<link rel="stylesheet" href="https://fonts.googleapis.com/css2?family=Inter:wght@400;600;700&display=swap">
<style>
  :root {
    --backdrop: #2e2a28;
    --card: #3f3f3f;
    --ink: #ffffff;
    --ink-soft: #e6e6e6;
    --rule: #d8d8d8;
  }
  * { box-sizing: border-box; margin: 0; padding: 0; }
  html, body {
    width: 1200px; height: 716px; overflow: hidden;
    background: var(--backdrop);
    font-family: "Inter", Arial, sans-serif;
    color: var(--ink);
  }
  .stage { position: relative; width: 1200px; height: 716px; }
  .card {
    position: absolute;
    width: 540px; height: 310px;
    background: var(--card);
    box-shadow: 0 10px 24px rgba(0,0,0,.45);
  }
  .card--front { left: 50px; top: 60px; padding: 52px 48px; }
  .card--back { left: 610px; top: 346px; }

  .holder-name { font-size: 26px; font-weight: 700; letter-spacing: -.2px; }
  .holder-title { font-size: 13px; font-weight: 400; color: var(--ink-soft); margin-top: 4px; }
  .contact { list-style: none; margin-top: 22px; font-size: 13px; }
  .contact li { display: flex; align-items: center; gap: 8px; margin-bottom: 6px; }
  .contact svg { width: 11px; height: 11px; flex: none; fill: var(--ink); }

  .appointment-title {
    position: absolute; left: 250px; top: 78px;
    font-size: 22px; font-weight: 700; letter-spacing: .5px;
  }
  .appointment-fields { position: absolute; left: 40px; top: 140px; width: 450px; list-style: none; }
  .appointment-fields li { display: flex; align-items: flex-end; height: 34px; font-size: 13px; }
  .field-label { width: 50px; }
  .field-line { flex: 1; border-bottom: 1px dashed var(--rule); margin-bottom: 3px; }
</style>
</head>
<body>
<main class="stage">
  <section class="card card--front" aria-label="Card front">
    <h1 class="holder-name">Dr Marlo Vintner</h1>
    <p class="holder-title">Doctor of Dental Medicine</p>
    <ul class="contact">
      <li>
        <svg viewBox="0 0 24 24" aria-hidden="true"><path d="M6.6 10.8a15.1 15.1 0 0 0 6.6 6.6l2.2-2.2a1 1 0 0 1 1-.25 11.4 11.4 0 0 0 3.6.57 1 1 0 0 1 1 1V20a1 1 0 0 1-1 1A17 17 0 0 1 3 4a1 1 0 0 1 1-1h3.5a1 1 0 0 1 1 1c0 1.25.2 2.45.57 3.57a1 1 0 0 1-.25 1z"/></svg>
        514-629-5074
      </li>
      <li>
        <svg viewBox="0 0 24 24" aria-hidden="true"><path d="M12 2a7 7 0 0 0-7 7c0 5.25 7 13 7 13s7-7.75 7-13a7 7 0 0 0-7-7zm0 9.5A2.5 2.5 0 1 1 12 6.5a2.5 2.5 0 0 1 0 5z"/></svg>
        5182 Ch. Birchfield Montreal QC H2T 4B9
      </li>
    </ul>
  </section>

  <section class="card card--back" aria-label="Card back">
    <h2 class="appointment-title">APPOINTMENT</h2>
    <ul class="appointment-fields">
      <li><span class="field-label">For:</span><span class="field-line"></span></li>
      <li><span class="field-label">Date:</span><span class="field-line"></span></li>
      <li><span class="field-label">Time:</span><span class="field-line"></span></li>
    </ul>
  </section>
</main>
</body>
</html>
```